Stationary and Business Card for eDiscovery Tech Company
Varendra Systems
Stationary and Business Card for eDiscovery Tech Company - Software
Creative Brief
Professional
Marcus T. Hellerby
Chief Executive Officer
48712 Larkspur Mill Rd Suite K340 - 500 Katy, TX 77494
tkolvern@varendra.example
www.varendra.example
In general: Our company is currently focused on providing software solutions to the legal industry for electronic discovery. While our company is forward thinking in its technology we still embrace conservative business standards, professionalism is key. For the business card: We want a clean design that is not cluttered. Omitting the mailing address would be acceptable. We have both stacked and side by side layouts of our logo, feel free to use either and be creative. We are considering the inclusion of a QR code, possibly on the back of the card unless it can be done well in the front design. IF it needs to be done on the back we would like to include a line of explanation such as "Contact information provided in QR code format for your convenience". The initial perception by the recipient of the card is important to us. We are considering moderate weight, linen textured cards (any insight as to complications with a linen texture card from a design perspective, please let me know) We are also considering the use of a card with rounded edges (In the event this should be taken into consideration for your design options) For the letterhead/stationary and envelope: We will need Microsoft Word template/document of the winning design for these items as well. Please do not hesitate to ask any questions. I look forward to working with you.
Possibly a QR code containing contact information.
tkolvern tkolvern
Cards which are heavily bisected with a large logo on one side and lots of stacks stacked on the opposite side seem cluttered and not something desired for this project. Additionally, I am finding designs which are using a colored background where the majority of the text is in white are more difficult to read.
I have come to realize my request to include a line of text with the QR code was a really bad idea. Please disregard using any decriptive text about including contact information by the qr code.

```html
<!DOCTYPE html>
<html lang="en">
<head>
<meta charset="utf-8">
<title>Varendra Systems – Business Card</title>
<link href="https://fonts.googleapis.com/css2?family=Open+Sans:wght@400;600;700&display=swap" rel="stylesheet">
<style>
  :root {
    --bg-top: #b9bcbf;
    --bg-bottom: #8f9396;
    --card: #fbfbfb;
    --ink: #3b3f44;
    --ink-soft: #6b7076;
    --brand: #2a5f8f;
    --navy: #1d3f63;
    --blue: #3c88c4;
    --sky: #5fa9dc;
    --steel: #9a9ea3;
    --steel-light: #d4d6d9;
  }
  * { box-sizing: border-box; margin: 0; padding: 0; }
  html, body { width: 1200px; height: 895px; overflow: hidden; }
  body {
    font-family: "Open Sans", Arial, sans-serif;
    background: linear-gradient(180deg, var(--bg-top), var(--bg-bottom));
    position: relative;
  }
  .card {
    position: absolute;
    top: 293px;
    width: 540px;
    height: 309px;
    background: var(--card);
    border-radius: 4px;
    box-shadow: 0 6px 18px rgba(0,0,0,.25);
    overflow: hidden;
  }
  .card--front { left: 40px; }
  .card--back  { left: 620px; }

  .brand {
    display: flex;
    align-items: center;
    gap: 12px;
  }
  .brand__mark {
    width: 34px; height: 34px;
    border-radius: 50%;
    background: var(--brand);
    flex: none;
  }
  .brand__name {
    font-weight: 700;
    color: var(--brand);
    letter-spacing: .5px;
    text-transform: uppercase;
    line-height: 1;
  }

  .card--front .brand { position: absolute; left: 34px; top: 36px; }
  .card--front .brand__name { font-size: 26px; }

  .identity {
    position: absolute;
    left: 34px; top: 140px;
    display: flex;
    align-items: baseline;
    gap: 10px;
    color: var(--ink);
  }
  .identity__name { font-size: 19px; font-weight: 700; }
  .identity__divider { font-size: 20px; font-weight: 400; }
  .identity__title { font-size: 14px; font-weight: 600; color: var(--ink-soft); }
  .address {
    position: absolute;
    left: 34px; top: 172px;
    font-size: 11.5px;
    font-weight: 600;
    color: var(--ink-soft);
  }

  .contact-band {
    position: absolute;
    left: 0; right: 0; bottom: 34px;
    height: 34px;
    display: flex;
    align-items: center;
    background: linear-gradient(90deg, var(--navy) 0%, var(--blue) 55%, var(--sky) 100%);
    padding-left: 24px;
    gap: 18px;
  }
  .contact {
    display: flex;
    align-items: center;
    gap: 6px;
    color: #fff;
    font-size: 11.5px;
    font-weight: 600;
  }
  .contact svg { width: 14px; height: 14px; flex: none; }
  .contact--email {
    margin-left: auto;
    margin-right: 14px;
    background: var(--navy);
    border-radius: 12px;
    padding: 4px 12px;
  }

  .web-strip {
    position: absolute;
    left: 0; top: 26px;
    width: 250px; height: 24px;
    background: linear-gradient(180deg, var(--steel-light), var(--steel));
    border-radius: 0 12px 12px 0;
    display: flex;
    align-items: center;
    padding-left: 26px;
    color: #fff;
    font-size: 11.5px;
    font-weight: 600;
    letter-spacing: .4px;
  }
  .card--back .brand {
    position: absolute;
    left: 50%; top: 50%;
    transform: translate(-50%, -50%);
    flex-direction: column;
    gap: 10px;
  }
  .card--back .brand__mark { width: 44px; height: 44px; }
  .card--back .brand__name { font-size: 30px; text-align: center; }
</style>
</head>
<body>

<section class="card card--front" aria-label="Business card front">
  <div class="brand">
    <span class="brand__mark"></span>
    <span class="brand__name">Varendra Systems</span>
  </div>

  <div class="identity">
    <span class="identity__name">Marcus T. Hellerby</span>
    <span class="identity__divider">|</span>
    <span class="identity__title">Chief Executive Officer</span>
  </div>
  <p class="address">48712 Larkspur Mill Rd Suite K340 - 500</p>

  <div class="contact-band">
    <span class="contact">
      <svg viewBox="0 0 16 16"><circle cx="8" cy="8" r="8" fill="#fff"/><path d="M5.2 4.2l1.4-.3.8 2-1 .7a5 5 0 0 0 2.7 2.7l.7-1 2 .8-.3 1.4c-3.4.3-6.5-2.8-6.3-6.3z" fill="#1d3f63"/></svg>
      012 555 0147
    </span>
    <span class="contact">
      <svg viewBox="0 0 16 16"><circle cx="8" cy="8" r="8" fill="#fff"/><rect x="5" y="3.5" width="6" height="9" rx="1" fill="#3c88c4"/><rect x="6" y="4.8" width="4" height="5.4" fill="#fff"/></svg>
      012 555 0183
    </span>
    <span class="contact contact--email">
      <svg viewBox="0 0 16 16"><circle cx="8" cy="8" r="8" fill="#fff"/><rect x="4" y="5" width="8" height="6" rx="1" fill="#1d3f63"/><path d="M4.3 5.4L8 8.3l3.7-2.9" stroke="#fff" stroke-width="1" fill="none"/></svg>
      tkolvern@varendra.example
    </span>
  </div>
</section>

<section class="card card--back" aria-label="Business card back">
  <div class="web-strip">www.varendra.example</div>
  <div class="brand">
    <span class="brand__mark"></span>
    <span class="brand__name">Varendra Systems</span>
  </div>
</section>

</body>
</html>
```